velmorino.eu :: Design ideas (no coding) for key pages of Personalized greeting cards online store

We need your vision on modern, clean, easy to read user interface (UI) for online service of personalized printed products, like greeting cards, postcards, fridge magnets, clips and etc.
Your vision should include UI presentation for:
- Home page with login (including soc nets)
- Product Designer page
- Cart pages (products and address selection)
- Example of general internal page (pricing, terms, etc)
- Artist info and portfolio page
We are looking for ideas we will love, NOT complete design of a whole site.
Top design/vision will we used as a basement for separate contract on complete design of the site.

UI should be based on existing functionality with some extent. It should not break ideas or methods used on prototype but designers are free to offer own product presentations, designer’s layout and cart views.

Prototype:
English: http://velmorino.eu
Russian: http://velmorino.ru
Lithuanian: http://velmorino.lt

Target Market(s)

People of 16-45 y.o. who likes to be distinctive, personal.

Industry/Entity Type

Store

Requirements
Must have
• Your work should meet attached requirements.
Site is multilingual. Wording should assume varieties in length on different languages.
Clean and easy to read UI
Flat design preferrably
Should be based on assets which are free or available for royalty-free licensing
Should not have
• heavy, meaningless 3D and shadow effects
Show NOT copy sites like: plonkra.com, tarnwick.co.uk

```html
<!DOCTYPE html>
<html lang="en">
<head>
<meta charset="utf-8">
<title>velmorino – Greeting Cards</title>
<link href="https://fonts.googleapis.com/css2?family=Source+Sans+3:wght@400;600;700&display=swap" rel="stylesheet">
<style>
:root{
  --page:#f8d6d3;
  --panel:#fde9e3;
  --brand:#9e1c1c;
  --coral:#ee6152;
  --navy:#2e5a7a;
  --teal:#22958e;
  --orange:#f47b20;
  --ink:#3a2a2a;
  --muted:#7a6a6a;
  --green:#6cae3c;
}
*{box-sizing:border-box;margin:0;padding:0}
html,body{width:1200px;height:902px;overflow:hidden}
body{background:#fff;font-family:"Source Sans 3",Arial,sans-serif;color:var(--ink);position:relative}
.frame{position:absolute;left:12px;top:0;width:1176px;height:893px;background:var(--page)}
.band{position:absolute;left:12px;width:1176px;background:linear-gradient(120deg,#f7cbb0,#fbe2c8 35%,#f3c9c0 60%,#f9dcc0)}
.band-top{top:0;height:121px;box-shadow:0 2px 3px rgba(0,0,0,.15)}
.band-bottom{top:779px;height:114px}
.logo{position:absolute;left:143px;top:36px;display:flex;flex-direction:column;align-items:center;gap:6px}
.logo-mark{width:40px;height:40px;background:var(--brand)}
.logo-name{font-size:17px;color:var(--brand);font-weight:400}
.headline{position:absolute;left:223px;top:18px;font-size:19px;font-weight:700;color:var(--brand)}
.auth{position:absolute;top:22px;height:18px;background:var(--brand);color:#fff;font-size:11px;line-height:18px;text-align:center}
.auth.signup{left:850px;width:56px}
.auth.login{left:921px;width:56px}
.auth.login::after{content:"";display:inline-block;margin-left:6px;border:4px solid transparent;border-top-color:#fff;vertical-align:-2px}
.side-links{position:absolute;left:994px;top:64px;list-style:none;font-size:8px;color:var(--brand);line-height:16px}
.side-links li::before{content:"";display:inline-block;width:9px;height:7px;background:var(--brand);margin-right:6px;vertical-align:-1px}
.nav{position:absolute;left:223px;top:54px;width:754px;height:122px;background:var(--panel);box-shadow:0 2px 4px rgba(0,0,0,.2)}
.nav-item{position:absolute;top:14px;width:130px;margin-left:-65px;text-align:center;font-size:15px;font-weight:700}
.nav-item svg{display:block;margin:0 auto 8px}
.nav-item.medias{left:106px;color:var(--coral)}
.nav-item.post{left:242px;color:var(--navy)}
.nav-item.greet{left:377px;color:var(--teal)}
.nav-item.square{left:512px;color:var(--orange)}
.nav-item.create{left:647px;color:var(--brand)}
.caret{display:block;margin:3px auto 0;width:0;border:7px solid transparent;border-top-color:currentColor;border-bottom:0}
.sub-all{position:absolute;left:377px;top:100px;width:130px;margin-left:-65px;text-align:center;font-size:10px;font-weight:600;color:var(--teal)}
.dropdown{position:absolute;top:141px;width:94px;height:111px;list-style:none;padding-top:6px;text-align:center;font-size:10px;font-weight:600;color:#fff;z-index:3;box-shadow:0 2px 3px rgba(0,0,0,.25)}
.dropdown li{height:19px;line-height:19px}
.dropdown.medias{left:282px;background:var(--coral)}
.dropdown.medias .active{background:var(--panel);color:var(--coral)}
.dropdown.post{left:418px;background:var(--navy)}
.dropdown.post .active{background:var(--panel);color:var(--navy)}
.swatches{position:absolute;left:223px;display:flex;gap:6.3px}
.swatches span{width:20px;height:20px;box-shadow:0 1px 2px rgba(0,0,0,.25);border:2px solid #fff}
.swatches .on{border-color:var(--brand)}
.row1{top:199px}.row2{top:226px}
.filter{position:absolute;left:223px;top:267px;width:754px;height:169px;background:var(--panel);box-shadow:0 2px 4px rgba(0,0,0,.2)}
.tag-box{position:absolute;left:16px;top:17px;width:722px;height:54px;background:#fff;border:1px solid #e9d6d0;padding:6px 8px;display:flex;gap:18px;align-items:flex-start}
.tag{font-size:15px;color:#555;background:#f3ecec;padding:0 4px;display:flex;align-items:center;gap:6px}
.tag i{width:15px;height:15px;background:var(--brand);color:#fff;font-style:normal;font-size:12px;line-height:15px;text-align:center;font-weight:700}
.add{position:absolute;left:718px;top:52px;width:20px;height:20px;background:var(--green);color:#fff;font-size:18px;line-height:19px;text-align:center;font-weight:700}
.themes{position:absolute;left:14px;top:80px;width:730px;line-height:32px;font-weight:600;color:var(--muted)}
.themes span{margin-right:6px;vertical-align:baseline}
.cards{position:absolute;top:463px;left:0}
.card{position:absolute;width:133px;background:#fff;box-shadow:0 1px 3px rgba(0,0,0,.3)}
.art{display:block;width:100%}
.info{padding:4px 6px 0;font-size:8px;color:var(--muted);line-height:11px;position:relative}
.artist{color:var(--brand);font-weight:700}
.price{position:absolute;right:6px;font-size:13px;color:var(--brand)}
.home{position:absolute;left:6px;width:14px;height:12px;background:#888}
.stripe{position:absolute;left:0;bottom:0;height:4px;width:100%;background:linear-gradient(90deg,#e57373 0 12%,#ffb74d 12% 24%,#4db6ac 24% 36%,#7986cb 36% 48%,#aed581 48% 60%,#f06292 60% 72%,#4fc3f7 72% 84%,#ffd54f 84%)}
.copy{position:absolute;left:16px;top:787px;font-size:8px;color:var(--muted)}
.footer-nav{position:absolute;top:857px;left:0;width:1200px;text-align:center;font-size:13px;color:var(--brand)}
.footer-nav a{color:var(--brand);text-decoration:none;padding:0 8px}
.footer-nav a:first-child{color:var(--ink)}
.footer-nav b{font-weight:400}
</style>
</head>
<body>
<div class="frame"></div>
<div class="band band-top" role="img" aria-label="Soft faceted triangle pattern in peach and pink"></div>
<div class="band band-bottom" role="img" aria-label="Soft faceted triangle pattern in peach and pink"></div>

<header>
  <div class="logo"><span class="logo-mark"></span><span class="logo-name">velmorino</span></div>
  <h1 class="headline">The Individual Greeting Cards According to your mood</h1>
  <a class="auth signup">Sign Up</a>
  <a class="auth login">Log In</a>
  <ul class="side-links"><li>Shopping Cart ( 5 )</li><li>Gift Card ( 5 )</li><li>Favorites ( 5 )</li></ul>
</header>

<nav class="nav">
  <div class="nav-item medias">
    <svg width="30" height="42" viewBox="0 0 30 42"><g fill="none" stroke="currentColor" stroke-width="3"><line x1="6" y1="2" x2="22" y2="30"/><line x1="24" y1="2" x2="8" y2="30"/><circle cx="7" cy="35" r="5"/><circle cx="23" cy="35" r="5"/></g></svg>All Medias
  </div>
  <div class="nav-item post">
    <svg width="40" height="42" viewBox="0 0 40 42"><rect x="3" y="2" width="26" height="24" fill="currentColor"/><rect x="12" y="14" width="26" height="26" fill="currentColor" stroke="#fde9e3" stroke-width="2"/></svg>PostCards
  </div>
  <div class="nav-item greet">
    <svg width="40" height="42" viewBox="0 0 40 42"><rect x="6" y="2" width="26" height="34" fill="currentColor"/><path d="M4 8 L22 12 L22 41 L4 37Z" fill="#1a7570"/></svg>Greeting Cards<span class="caret"></span>
  </div>
  <div class="nav-item square">
    <svg width="40" height="42" viewBox="0 0 40 42"><rect x="4" y="4" width="32" height="36" fill="currentColor"/></svg>Square Cards<span class="caret"></span>
  </div>
  <div class="nav-item create">
    <svg width="40" height="42" viewBox="0 0 40 42"><path d="M8 4 H30 V20 M30 30 V40 H8Z" fill="none" stroke="currentColor" stroke-width="3"/><path d="M18 30 L32 14 L36 18 L22 33 L17 34Z" fill="currentColor"/></svg>Create Card
  </div>
  <div class="sub-all">All Formats</div>
</nav>

<ul class="dropdown medias"><li>All Formats</li><li class="active">Standard Cards</li><li>Mini Card</li><li>Nano Card</li></ul>
<ul class="dropdown post"><li>All Formats</li><li>Standard Cards</li><li>Mini Card</li><li class="active">Nano Card</li></ul>

<div class="swatches row1">
  <span style="background:#f7e04a"></span><span style="background:#f0b429"></span><span style="background:#e89b3c"></span><span style="background:#c94f3c"></span><span style="background:#d9534f"></span><span style="background:#c2603a"></span><span style="background:#e0702a"></span><span style="background:#cf4d3e"></span><span style="background:#a9b84a"></span><span style="background:#8aac3a"></span><span style="background:#5a5a50"></span><span style="background:#3f6b4c"></span><span style="background:#3b6a5a"></span><span style="background:#2e4a6e"></span><span style="background:#4a4a9a"></span><span style="background:#5b3e8a"></span><span style="background:#7a3e6a"></span><span style="background:#8b3a2e"></span><span class="on" style="background:#e8641e"></span><span style="background:#d9534f"></span><span style="background:#e4762a"></span><span style="background:#f0a020"></span><span style="background:#f5e02a"></span><span style="background:#222"></span><span style="background:#fff"></span><span style="background:linear-gradient(90deg,#e57373 50%,#4db6ac 50%)"></span>
</div>
<div class="swatches row2">
  <span style="background:linear-gradient(90deg,#4fc3f7 50%,#ffd54f 50%)"></span><span style="background:#fff"></span><span style="background:#333"></span><span style="background:#7a6a60"></span><span style="background:#c94f3c"></span><span style="background:#e0702a"></span><span style="background:#9a6a3a"></span><span style="background:#3f5a8a"></span><span style="background:#4a4a9a"></span><span style="background:#2e4a6e"></span><span style="background:#3a5a4a"></span><span style="background:#3f6b4c"></span><span style="background:#4a7a5a"></span><span class="on" style="background:#9ab82a"></span><span style="background:#8ac06a"></span><span style="background:#6a9a8a"></span><span style="background:#6a7ab0"></span><span style="background:#6a9ae0"></span><span style="background:#8a6ac0"></span><span style="background:#3a7a6a"></span><span style="background:#d96a4a"></span><span style="background:#f0b040"></span><span style="background:#f0a090"></span><span style="background:#f5e04a"></span><span style="background:#f0c040"></span><span style="background:#f7e44a"></span>
</div>

<section class="filter">
  <div class="tag-box">
    <span class="tag">All<i>×</i></span><span class="tag">Bears<i>×</i></span><span class="tag">Congratulations<i>×</i></span><span class="tag">Birthday Cards<i>×</i></span><span class="tag">Photos<i>×</i></span>
  </div>
  <span class="add">+</span>
  <p class="themes">
    <span style="font-size:16px;color:var(--brand);font-weight:400">Themes:</span>
    <span style="font-size:15px;color:#a8c8f0">All</span>
    <span style="font-size:10px;color:#e8664a">Bears</span>
    <span style="font-size:13px;color:#8ac04a">Birthday Cards</span>
    <span style="font-size:13px;color:var(--teal)">Cats</span>
    <span style="font-size:25px;color:#f0a820;font-weight:700">Congratulations !</span>
    <span style="font-size:13px;color:#e8664a">Dogs</span>
    <span style="font-size:10px;color:var(--teal)">Flowers</span>
    <span style="font-size:16px;color:#8ac04a">For children</span>
    <span style="font-size:8px;color:#c8402a">Friendship</span>
    <span style="font-size:15px;color:#f0a0a0">Love</span><br>
    <span style="font-size:25px;color:#5a5a9a;font-weight:700">Newborn</span>
    <span style="font-size:10px;color:#f0a820">Photos</span>
    <span style="font-size:13px;color:var(--teal)">Religion</span>
    <span style="font-size:16px;color:#8b3a1e;font-weight:700">Valentine's day</span>
  </p>
</section>

<main class="cards">
  <article class="card" style="left:223px;height:278px">
    <div class="art" style="height:203px;background:linear-gradient(160deg,#cfe3f2,#f3eee6 50%,#b7cfe7)" role="img" aria-label="Pastel illustration of a teddy bear with hearts"></div>
    <div class="info"><div class="artist">Mart Olsen</div>Egle | Zvaigzdes Kaledos<br>Naujieji | Metai</div>
    <span class="home" style="bottom:12px"></span><span class="price" style="bottom:10px">€ 2.99</span><span class="stripe"></span>
  </article>
  <article class="card" style="left:377px;height:209px">
    <div class="art" style="height:135px;background:linear-gradient(135deg,#1a3aa8,#2f5fd0 50%,#1a2f8a)" role="img" aria-label="Festive tiles with trees and stars on blue"></div>
    <div class="info"><div class="artist">Mart Olsen</div>Egle | Zvaigzdes Kaledos<br>Naujieji | Metai</div>
    <span class="home" style="bottom:12px"></span><span class="price" style="bottom:10px">€ 2.99</span><span class="stripe"></span>
  </article>
  <article class="card" style="left:533px;height:272px">
    <div class="art" style="height:196px;background:linear-gradient(160deg,#6a4a2e,#b58a5a 45%,#3a2e4a)" role="img" aria-label="Painted nativity scene in warm browns"></div>
    <div class="info"><div class="artist">Mart Olsen</div>Egle | Zvaigzdes Kaledos<br>Naujieji | Metai</div>
    <span class="home" style="bottom:12px"></span><span class="price" style="bottom:10px">€ 2.99</span><span class="stripe"></span>
  </article>
  <article class="card" style="left:689px;height:272px">
    <div class="art" style="height:196px;background:radial-gradient(circle at 50% 45%,#e8e0c8,#c8322a 45%,#b0201e)" role="img" aria-label="White flower bouquet on red background"></div>
    <div class="info"><div class="artist">Mart Olsen</div>Egle | Zvaigzdes Kaledos<br>Naujieji | Metai</div>
    <span class="home" style="bottom:12px"></span><span class="price" style="bottom:10px">€ 2.99</span><span class="stripe"></span>
  </article>
  <article class="card" style="left:844px;height:272px">
    <div class="art" style="height:196px;background:linear-gradient(160deg,#6a4a2e,#b58a5a 45%,#3a2e4a)" role="img" aria-label="Painted nativity scene in warm browns"></div>
    <div class="info"><div class="artist">Mart Olsen</div>Egle | Zvaigzdes Kaledos<br>Naujieji | Metai</div>
    <span class="home" style="bottom:12px"></span><span class="price" style="bottom:10px">€ 2.99</span><span class="stripe"></span>
  </article>
</main>

<footer>
  <p class="copy">© 2014 velmorino</p>
  <nav class="footer-nav"><a>About Us</a><b>|</b><a>How It Works</a><b>|</b><a>Prices</a><b>|</b><a>Rules</a><b>|</b><a>Contacts</a></nav>
</footer>
</body>
</html>
```